Full set of animated banner ads for Wrixel

Wrixel requires a full set of animated banner ads for our new blog package product:

https://uk.wrixel-example.com/blog-packages

Key USPs

A blog which has regular content attracts more visitors. If a business does not have time to do this, our new product is the perfect solution. We'll supply unique, quality blog posts direct to your blog each week. Cancel or change plan any time.

Call to action

Signup to a package, enter a few details and we'll start immediately.

Specs

.GIF preferred over .SWF.
150 KB or less

Show us a couple of examples so we can pick a winner. Once we decide a winner please be ready to send files in the following sizes;

468 × 60 Banner
728 × 90 Leaderboard
250 × 250 Square
200 × 200 Small square
336 × 280 Large rectangle
300 × 250 Inline rectangle
120 × 600 Skyscraper
160 × 600 Wide skyscraper
300 × 600 Half-page ad
970 × 90 Large leaderboard
240 × 400 Vertical rectangle
980 × 120 Panorama
930 × 180 Top banner
250 × 360 Triple widescreen
580 × 400 Netboard
970 × 250 Billboard

Target Market(s)

small business owners

Industry/Entity Type

Business

```html
<!DOCTYPE html>
<html lang="en">
<head>
<meta charset="utf-8">
<title>Wrixel – Blogging Made Easy banners</title>
<link href="https://fonts.googleapis.com/css2?family=Open+Sans:wght@400;600;700&display=swap" rel="stylesheet">
<style>
  :root{
    --backdrop:#4a1d0f;
    --panel-dark:#242424;
    --panel-edge:#0f0f0f;
    --price-bg:#f0f0f0;
    --brand-green:#62ad3d;
    --green-text:#5aa834;
    --ink:#2a2a2a;
    --ink-soft:#3a3a3a;
    --white:#ffffff;
    --button-top:#7cc24f;
    --button-bottom:#4f9a2c;
  }
  *{box-sizing:border-box;margin:0;padding:0}
  html,body{width:1200px;height:1081px;overflow:hidden}
  body{background:var(--backdrop);font-family:"Open Sans",Arial,sans-serif;position:relative}

  .banner{position:absolute;top:94px;width:231px;height:865px;border:1px solid var(--panel-edge);overflow:hidden;background:var(--brand-green)}
  .banner--package{left:179px}
  .banner--content{left:429px}
  .banner--publish{left:681px}

  .headline{position:absolute;top:0;left:0;right:0;height:106px;background:var(--panel-dark);
    color:var(--white);text-align:center;text-transform:uppercase;font-weight:600;font-size:33px;
    line-height:36px;letter-spacing:-1px;padding-top:16px}
  .headline em{font-style:normal;color:var(--brand-green);font-weight:700}
  .headline-pointer{position:absolute;left:50%;bottom:-14px;margin-left:-13px;width:26px;height:14px}

  .price{position:absolute;top:106px;left:0;right:0;height:144px;background:var(--price-bg);
    text-align:center;color:var(--ink-soft);text-transform:uppercase}
  .price-lead{display:block;font-size:26px;line-height:28px;margin-top:16px}
  .price-amount{display:block;font-size:60px;font-weight:700;line-height:58px;color:var(--green-text)}
  .price-period{display:block;font-size:28px;line-height:30px}

  .pitch{position:absolute;top:250px;left:0;right:0;height:448px}
  .pitch-title{text-align:center;font-weight:600;font-size:30px;line-height:28px;color:var(--ink);letter-spacing:-0.5px}
  .banner--package .pitch-title{margin-top:50px}
  .banner--content .pitch-title,.banner--publish .pitch-title{margin-top:33px}
  .banner--publish .pitch-title{line-height:33px}
  .pitch-list{list-style:none;margin:24px 0 0 33px;color:var(--ink);font-size:20px;line-height:21px}
  .banner--package .pitch-list li{margin-bottom:15px}
  .banner--content .pitch-list,.banner--publish .pitch-list{margin-top:28px}
  .banner--content .pitch-list li,.banner--publish .pitch-list li{margin-bottom:6px}
  .pitch-list li{position:relative;padding-left:13px}
  .pitch-list li::before{content:"";position:absolute;left:0;top:8px;width:6px;height:6px;background:var(--white)}

  .visual{position:absolute}
  .banner--package .visual{left:0;right:0;top:231px;height:217px;background:linear-gradient(#3a3a3a,#f3f1e6 18%,#eeeadb 85%,#9a9a9a)}
  .banner--content .visual{left:0;right:0;top:242px;height:173px;background:linear-gradient(135deg,#c9b9a8,#6f5f57 55%,#e7ddd2)}
  .banner--publish .visual{left:10px;width:211px;top:256px;height:159px;border-radius:6px;background:linear-gradient(#3b3b3b,#f2f2f2 20%,#e4e4e4 85%,#3b3b3b)}

  .footer{position:absolute;top:698px;left:0;right:0;bottom:0;background:var(--panel-dark);border-top:2px solid #151515}
  .brand{position:absolute;top:42px;left:0;right:0;display:flex;align-items:center;justify-content:center;gap:10px}
  .brand-dot{width:22px;height:22px;border-radius:50%;background:var(--brand-green)}
  .brand-name{color:var(--white);font-weight:700;font-size:36px;line-height:40px;letter-spacing:-0.5px}
  .signup{position:absolute;top:110px;left:38px;width:156px;height:38px;border-radius:4px;
    background:linear-gradient(var(--button-top),var(--button-bottom));border:1px solid #2f6a16;
    display:flex;align-items:center;justify-content:center;gap:10px;color:#111;font-size:23px;text-transform:uppercase;letter-spacing:-0.5px}
  .signup svg{width:22px;height:22px}
</style>
</head>
<body>

<section class="banner banner--package">
  <h2 class="headline">Blogging<br>made <em>easy</em>
    <svg class="headline-pointer" viewBox="0 0 26 14"><polygon points="0,0 26,0 13,14" fill="#242424"/></svg></h2>
  <div class="price"><span class="price-lead">From just</span><span class="price-amount">£49</span><span class="price-period">a month</span></div>
  <div class="pitch">
    <h3 class="pitch-title">Choose<br>your package</h3>
    <ul class="pitch-list"><li>how many posts</li><li>what subjects</li></ul>
    <div class="visual" role="img" aria-label="Laptop showing the Wrixel order dashboard"></div>
  </div>
  <div class="footer">
    <div class="brand"><span class="brand-dot"></span><span class="brand-name">Wrixel</span></div>
    <a class="signup">Sign up <svg viewBox="0 0 22 22"><circle cx="11" cy="11" r="10" fill="#111"/><path d="M5 9h6V5l7 6-7 6v-4H5z" fill="#7cc24f"/></svg></a>
  </div>
</section>

<section class="banner banner--content">
  <h2 class="headline">Blogging<br>made <em>easy</em>
    <svg class="headline-pointer" viewBox="0 0 26 14"><polygon points="0,0 26,0 13,14" fill="#242424"/></svg></h2>
  <div class="price"><span class="price-lead">From just</span><span class="price-amount">£49</span><span class="price-period">a month</span></div>
  <div class="pitch">
    <h3 class="pitch-title">We create<br>your content</h3>
    <ul class="pitch-list"><li>we find the right copywriter</li><li>we create blog posts</li></ul>
    <div class="visual" role="img" aria-label="Collage of portrait photos of the copywriting team"></div>
  </div>
  <div class="footer">
    <div class="brand"><span class="brand-dot"></span><span class="brand-name">Wrixel</span></div>
    <a class="signup">Sign up <svg viewBox="0 0 22 22"><circle cx="11" cy="11" r="10" fill="#111"/><path d="M5 9h6V5l7 6-7 6v-4H5z" fill="#7cc24f"/></svg></a>
  </div>
</section>

<section class="banner banner--publish">
  <h2 class="headline">Blogging<br>made <em>easy</em>
    <svg class="headline-pointer" viewBox="0 0 26 14"><polygon points="0,0 26,0 13,14" fill="#242424"/></svg></h2>
  <div class="price"><span class="price-lead">From just</span><span class="price-amount">£49</span><span class="price-period">a month</span></div>
  <div class="pitch">
    <h3 class="pitch-title">Instant<br>publishing</h3>
    <ul class="pitch-list"><li>posts delivered weekly</li><li>regular content for your blog</li></ul>
    <div class="visual" role="img" aria-label="Tablet showing the order export screen, magnified"></div>
  </div>
  <div class="footer">
    <div class="brand"><span class="brand-dot"></span><span class="brand-name">Wrixel</span></div>
    <a class="signup">Sign up <svg viewBox="0 0 22 22"><circle cx="11" cy="11" r="10" fill="#111"/><path d="M5 9h6V5l7 6-7 6v-4H5z" fill="#7cc24f"/></svg></a>
  </div>
</section>

</body>
</html>
```